business cards, stationary
lets see what you got
Use specific fonts
up to designer
Modern
Calvin Marsh
Director of Sales
1870 Quarrymill road, Suite 114 Burlington, On L4K 3P8
Calvin@sunlanejourneys.example
www.sunlanejourneys.example
BBM: 58720936
LOGO on back

```html
<!DOCTYPE html>
<html lang="en">
<head>
<meta charset="utf-8">
<title>Sun Lane Journeys – Stationery</title>
<link rel="stylesheet" href="https://fonts.googleapis.com/css2?family=Source+Sans+3:wght@400;600;700&display=swap">
<style>
  :root {
    --purple: #5d2e82;
    --purple-deep: #4a2169;
    --green: #8cc63e;
    --paper: #ffffff;
    --ink: #3a3a3a;
    --muted: #777777;
    --backdrop: #e9e6e1;
    --line: #b9b9b9;
  }
  * { box-sizing: border-box; margin: 0; padding: 0; }
  html, body { width: 1200px; height: 935px; overflow: hidden; }
  body {
    background: var(--backdrop);
    font-family: "Source Sans 3", Arial, sans-serif;
    color: var(--ink);
    position: relative;
  }
  .sheet {
    position: absolute;
    background: var(--paper);
    box-shadow: 0 2px 8px rgba(0,0,0,.18);
    overflow: hidden;
  }
  .swoosh { position: absolute; left: 0; bottom: 0; width: 100%; }
  .brand-name {
    font-weight: 700;
    color: var(--purple);
    letter-spacing: -0.5px;
    white-space: nowrap;
  }
  .brand-dot {
    display: inline-block;
    border-radius: 50%;
    background: var(--green);
    vertical-align: middle;
  }

  /* Fax cover */
  .fax { left: 38px; top: 190px; width: 500px; height: 735px; }
  .fax .brand-name { position: absolute; left: 38px; top: 30px; font-size: 30px; }
  .fax-title { position: absolute; left: 40px; top: 135px; font-size: 40px; font-weight: 700; color: #222; }
  .fax-fields { position: absolute; left: 42px; top: 215px; width: 120px; list-style: none; }
  .fax-fields li {
    font-size: 11px; font-weight: 600; height: 38px; display: flex; align-items: flex-end;
    border-bottom: 1px solid var(--line); padding-bottom: 3px;
  }
  .fax-checks { position: absolute; left: 42px; top: 420px; display: flex; gap: 38px; font-size: 11px; }
  .fax-checks span::before {
    content: ""; display: inline-block; width: 9px; height: 9px; border: 1px solid var(--muted);
    margin-right: 6px; vertical-align: -1px;
  }
  .fax-footer { position: absolute; left: 100px; bottom: 18px; color: #fff; font-size: 9px; line-height: 1.5; }

  /* Letterhead */
  .letterhead { left: 190px; top: 38px; width: 680px; height: 870px; }
  .letterhead .brand-name { position: absolute; left: 38px; top: 22px; font-size: 34px; }
  .letterhead-footer {
    position: absolute; left: 120px; right: 40px; bottom: 22px; color: #fff;
    font-size: 9.5px; line-height: 1.55; display: flex; gap: 48px;
  }

  /* Envelope */
  .envelope { left: 520px; top: 340px; width: 635px; height: 245px; }
  .envelope-flap-text {
    position: absolute; right: 60px; top: 8px; font-size: 15px; font-weight: 700;
    color: var(--purple); transform: rotate(180deg); opacity: .8;
  }
  .envelope .brand-name { position: absolute; left: 22px; top: 62px; font-size: 30px; }
  .envelope-address { position: absolute; left: 24px; top: 100px; font-size: 9px; line-height: 1.4; }
  .envelope-web { position: absolute; right: 22px; bottom: 14px; color: #fff; font-size: 10px; font-weight: 600; }

  /* Business cards */
  .card { border-radius: 6px; }
  .card-front { left: 850px; top: 125px; width: 305px; height: 150px; }
  .card-front .brand-name { position: absolute; left: 22px; top: 14px; font-size: 19px; }
  .card-person { position: absolute; left: 22px; top: 48px; font-size: 8px; line-height: 1.45; }
  .card-person strong { font-size: 9px; letter-spacing: .5px; text-transform: uppercase; display: block; }
  .card-contact { position: absolute; left: 22px; right: 14px; bottom: 10px; color: #fff; font-size: 7px; line-height: 1.5; }

  .card-web-side { left: 915px; top: 620px; width: 240px; height: 130px; }
  .card-web-side .brand-name { position: absolute; left: 18px; top: 12px; font-size: 17px; }
  .card-web-side .card-url { position: absolute; left: 18px; top: 44px; font-size: 7.5px; color: var(--muted); }

  .card-back { left: 800px; top: 775px; width: 265px; height: 140px; }
  .card-back-logo { position: absolute; left: 0; right: 0; top: 48px; text-align: center; }
  .card-back-logo .brand-name { font-size: 21px; }
  .card-back-url { position: absolute; left: 0; right: 0; top: 82px; text-align: center; font-size: 7.5px; color: var(--muted); }
</style>
</head>
<body>

<svg width="0" height="0" style="position:absolute" aria-hidden="true">
  <defs>
    <symbol id="swoosh" viewBox="0 0 400 100" preserveAspectRatio="none">
      <path d="M0,62 C120,40 260,22 400,4 L400,100 L0,100 Z" fill="#5d2e82"/>
      <path d="M0,56 C130,34 260,14 400,-4" fill="none" stroke="#ffffff" stroke-width="5"/>
      <path d="M0,50 C140,26 270,6 400,-12" fill="none" stroke="#8cc63e" stroke-width="7"/>
    </symbol>
  </defs>
</svg>

<section class="sheet fax">
  <div class="brand-name">sunlanejourneys</div>
  <h1 class="fax-title">FAX</h1>
  <ul class="fax-fields">
    <li>To :</li><li>Fax :</li><li>Phone :</li><li>Re :</li>
  </ul>
  <div class="fax-checks"><span>Urgent</span><span>For Review</span></div>
  <svg class="swoosh" height="150"><use href="#swoosh" width="100%" height="100%"/></svg>
  <div class="fax-footer">1870 Quarrymill road,<br>Suite 114 Burlington, On L4K 3P8</div>
</section>

<section class="sheet letterhead">
  <div class="brand-name">sunlanejourneys</div>
  <svg class="swoosh" height="210"><use href="#swoosh" width="100%" height="100%"/></svg>
  <div class="letterhead-footer">
    <div>1870 Quarrymill road,<br>Suite 114 Burlington, On L4K 3P8</div>
    <div>T 1.800.555.0142<br>F 905.555.0187</div>
    <div>Calvin@sunlanejourneys.example<br>www.sunlanejourneys.example</div>
  </div>
</section>

<section class="sheet envelope">
  <div class="envelope-flap-text">sunlanejourneys</div>
  <div class="brand-name">sunlanejourneys</div>
  <div class="envelope-address">1870 Quarrymill road<br>Suite 114, Burlington, On L4K 3P8</div>
  <svg class="swoosh" height="80"><use href="#swoosh" width="100%" height="100%"/></svg>
  <div class="envelope-web">www.sunlanejourneys.example</div>
</section>

<section class="sheet card card-front">
  <div class="brand-name">sunlanejourneys</div>
  <div class="card-person"><strong>Calvin Marsh</strong>Director of Sales<br>BBM: 58720936</div>
  <svg class="swoosh" height="55"><use href="#swoosh" width="100%" height="100%"/></svg>
  <div class="card-contact">1870 Quarrymill road, Suite 114 Burlington, On L4K 3P8 · Calvin@sunlanejourneys.example</div>
</section>

<section class="sheet card card-web-side">
  <div class="brand-name">sunlanejourneys</div>
  <div class="card-url">www.sunlanejourneys.example</div>
  <svg class="swoosh" height="60"><use href="#swoosh" width="100%" height="100%"/></svg>
</section>

<section class="sheet card card-back">
  <div class="card-back-logo"><span class="brand-name">sunlanejourneys</span></div>
  <div class="card-back-url">www.sunlanejourneys.example</div>
</section>

</body>
</html>
```